Custom Wordpress Theme Needed

We need a custom Wordpress theme built with the following features:

1. Flat style design
2. Fully responsive - built for mobile and tablets first; bootstrap or other framework used
3. Flexible - comes with homepage layouts for portfolios, agencies, and magazines
4. Built in 'contact' and 'about us' styling
5. Pre-populated pages and content, including reusable images
6. Multiple slider options

We are completely open to your creativity as far as the overall design style is concerned, but some of our favorites are:
http://themes.plovaro.com/themeselector/?theme=TideBoard
http://www.kelmora.ru/flatmagazine/
http://quarnwellbox.com/wp/velta/intro/
http://theme.dovrask.net/second/

Most unique and in-depth style wins!

Reason: We need more designs!

Reason: Waiting on final submissions and revisions. Thanks!

```html
<!DOCTYPE html>
<html lang="en">
<head>
<meta charset="utf-8">
<title>YourLogo — Home</title>
<link rel="stylesheet" href="https://fonts.googleapis.com/css2?family=Ubuntu:wght@400;500;700&family=Arimo:wght@400;700&display=swap">
<style>
  :root{
    --page:#8c8e9c;
    --nav-band:#55565f;
    --nav-text:#e4e5ee;
    --tab:#2b2f86;
    --logo:#16189a;
    --panel:#33333b;
    --panel-edge:#6b3a55;
    --accent:#5b63e2;
    --title-accent:#1a1fa6;
    --button:#262b86;
    --button-edge:#4c55c8;
    --link:#1a1fa6;
    --text:#ffffff;
    --muted:#dcdce4;
    --social:#7d7f8b;
    --social-edge:#9fa1ac;
    --divider:#4a53c4;
  }
  *{box-sizing:border-box;margin:0;padding:0}
  html,body{width:897px;height:1200px;overflow:hidden}
  body{background:var(--page);position:relative;font-family:"Arimo",Arial,sans-serif;color:var(--text)}
  .abs{position:absolute}

  .site-logo{left:65px;top:18px;font-family:"Ubuntu",sans-serif;font-weight:700;font-size:38px;color:var(--logo);letter-spacing:-0.5px}
  .social{display:flex;gap:5px}
  .social span{width:24px;height:24px;border-radius:50%;background:var(--social);border:1px solid var(--social-edge);display:block}
  .social-top{left:718px;top:50px}
  .social-foot{left:718px;top:1159px}

  .nav-band{left:0;top:90px;width:897px;height:32px;background:var(--nav-band);border-top:1px solid #e8e8ee;border-bottom:1px solid #a9aab4}
  .nav{position:absolute;left:64px;top:0;height:30px;display:flex;list-style:none;font-family:"Ubuntu",sans-serif;font-size:12.5px}
  .nav li{line-height:30px;color:var(--nav-text);padding:0 19px}
  .nav li.active{background:var(--tab);color:#fff}

  .hero{left:64px;top:122px;width:765px;height:359px;
    background:repeating-linear-gradient(135deg,rgba(255,255,255,.05) 0 2px,transparent 2px 5px),#8f91a0}
  .hero-media{left:5px;top:27px;width:300px;height:300px;border-radius:20px 20px 8px 8px;
    background:linear-gradient(180deg,#8a8dd0 0%,#6f72bf 55%,#9c9ed6 100%)}
  .hero-title{left:389px;top:54px;font-family:"Ubuntu",sans-serif;font-weight:500;font-size:36px;line-height:41px;color:#fff}
  .hero-title em{font-style:normal;color:var(--title-accent)}
  .hero-text{left:389px;top:149px;width:300px;font-size:10px;line-height:18px;color:#fff}
  .btn-hero{left:389px;top:251px;width:141px;height:40px;background:var(--button);border:1px solid var(--button-edge);
    box-shadow:0 0 12px rgba(255,255,255,.35);font-family:"Ubuntu",sans-serif;font-size:15px;line-height:38px;text-align:center;color:#fff}
  .dots{left:698px;top:324px;display:flex;gap:5px;align-items:center}
  .dots span{width:10px;height:10px;border-radius:50%;background:#24242c;display:block}
  .dots span.on{width:12px;height:12px;background:#1f2fd0;box-shadow:0 0 4px #6c7bff}

  .panel{left:64px;top:484px;width:765px;height:662px;background:var(--panel);border:1px solid var(--panel-edge);border-radius:6px}
  .heading{font-family:"Ubuntu",sans-serif;font-size:19.5px;color:var(--accent);text-transform:uppercase;white-space:nowrap}
  .service-text{width:200px;font-size:9.6px;line-height:16.3px;color:var(--muted)}
  .btn-small{height:20px;background:var(--button);border:1px solid var(--button-edge);font-size:9.6px;line-height:18px;text-align:center;color:#dfe0f4}
  .rule-h{left:64px;top:693px;width:765px;height:1px;background:linear-gradient(90deg,transparent,var(--divider) 20%,var(--divider) 80%,transparent)}
  .rule-v{left:447px;top:709px;width:1px;height:416px;background:linear-gradient(180deg,transparent,var(--divider) 15%,var(--divider) 85%,transparent)}

  .welcome-media{left:99px;top:773px;width:240px;height:144px;border:1px solid #8fb4e6;
    background:radial-gradient(ellipse at 60% 70%,#4fd0f2 0%,#1d6fcf 45%,#0c2a8c 100%)}
  .welcome-text{left:99px;top:930px;width:330px;font-size:9.8px;line-height:16.4px;color:#fff}

  .post{left:482px;width:240px}
  .post-date{font-size:14.6px;font-weight:700;line-height:18px;color:#fff}
  .post-text{font-size:9.6px;line-height:16.3px;color:#fff;margin-top:1px}
  .post-meta{font-size:9.6px;line-height:12px;color:var(--accent)}

  .footer-links{left:65px;top:1157px;font-size:10px;color:var(--link);word-spacing:1px}
  .copyright{left:64px;top:1178px;font-family:"Ubuntu",sans-serif;font-size:10px;color:var(--link)}
</style>
</head>
<body>
  <header>
    <div class="abs site-logo">YourLogo</div>
    <div class="abs social social-top" aria-label="Social links"><span></span><span></span><span></span><span></span></div>
    <nav class="abs nav-band">
      <ul class="nav">
        <li class="active">Home</li><li>About Us</li><li>Services</li><li>Blog</li><li>Gallery</li><li>Contact Us</li>
      </ul>
    </nav>
  </header>

  <section class="abs hero">
    <div class="abs hero-media" role="img" aria-label="Desktop monitor showing a businessman holding floating network icons"></div>
    <h1 class="abs hero-title">SOME BIG <em>TITLE</em><br>GOES HERE</h1>
    <p class="abs hero-text">Lorem ipsum dolor sit amet, consectetur adipiscing elit. Curabitur eget nibh id enim laoreet euismod eget ac orci. Vestibulum ante ipsum primis in faucibus orci luctus et ultrices posuere cubilia. Curae cras pellentesque euismod fringilla.</p>
    <div class="abs btn-hero">Know More</div>
    <div class="abs dots"><span></span><span class="on"></span><span></span><span></span></div>
  </section>

  <main class="abs panel"></main>

  <h2 class="abs heading" style="left:100px;top:522px">Services Here</h2>
  <p class="abs service-text" style="left:100px;top:566px">Lorem ipsum dolor sit amet, consectetur adipiscing elit. Curabitur eget nibh id enim laoreet euismod eget ac orci. Vestibulum anipsum primis in faucibus orci luctus.</p>
  <div class="abs btn-small" style="left:247px;top:647px;width:52px">More</div>

  <h2 class="abs heading" style="left:334px;top:522px">Services Here</h2>
  <p class="abs service-text" style="left:336px;top:566px">Lorem ipsum dolor sit amet, consectetur adipiscing elit. Curabitur eget nibh id enim laoreet euismod eget ac orci. Vestibulum anipsum primis in faucibus orci luctus.</p>
  <div class="abs btn-small" style="left:495px;top:647px;width:52px">More</div>

  <h2 class="abs heading" style="left:586px;top:522px">Services Here</h2>
  <p class="abs service-text" style="left:586px;top:566px">Lorem ipsum dolor sit amet, consectetur adipiscing elit. Curabitur eget nibh id enim laoreet euismod eget ac orci. Vestibulum anipsum primis in faucibus orci luctus.</p>
  <div class="abs btn-small" style="left:746px;top:647px;width:52px">More</div>

  <div class="abs rule-h"></div>
  <div class="abs rule-v"></div>

  <h2 class="abs heading" style="left:100px;top:735px">Welcome to our company</h2>
  <div class="abs welcome-media" role="img" aria-label="Silhouettes of business people standing before a blue world map"></div>
  <p class="abs welcome-text">Lorem ipsum dolor sit amet, consectetur adipiscing elit. Curabitur eget nibh id enim laoreet euismod eget ac orci. Vestibulum anipsum primis in faucibus orci luctus. et ultrices posuere cubilia Curae; Cras pellentesque euismod fringilla. Sed vitae ante lectus, non fringilla nibh. Aenean vitae odio ac risus aliquam malesuada. Quisque mollis mauris quis odio bibendum consectetur. Vestibulum venenatis odio dolor, nec pretium odio. quis dolor sapien, et gravida mauris.</p>
  <div class="abs btn-small" style="left:334px;top:1050px;width:79px">Read More</div>

  <h2 class="abs heading" style="left:483px;top:735px">Latest Blog</h2>
  <article class="abs post" style="top:788px">
    <div class="post-date">18 October, 2013</div>
    <p class="post-text">Lorem ipsum dolor sit amet, consectetur adipiscing elit. Curabitur eget nibh id enim laoreet euismod</p>
    <div class="post-meta">posted by Lorem ipsum</div>
  </article>
  <article class="abs post" style="top:874px">
    <div class="post-date">12 October, 2013</div>
    <p class="post-text">Lorem ipsum dolor sit amet, consectetur adipiscing elit. Curabitur eget nibh id enim laoreet euismod</p>
    <div class="post-meta">posted by Lorem ipsum</div>
  </article>
  <article class="abs post" style="top:957px">
    <div class="post-date">10 October, 2013</div>
    <p class="post-text">Lorem ipsum dolor sit amet, consectetur adipiscing elit. Curabitur eget nibh id enim laoreet euismod</p>
    <div class="post-meta">posted by Lorem ipsum</div>
  </article>
  <div class="abs btn-small" style="left:720px;top:1050px;width:79px">Read More</div>

  <footer>
    <div class="abs footer-links">Home &nbsp;| &nbsp;About Us &nbsp;| &nbsp;Services &nbsp;| &nbsp;Blog &nbsp;| &nbsp;Gallery &nbsp;| &nbsp;Contact Us</div>
    <div class="abs copyright">© Copyright 2013 - All rights reserved.</div>
    <div class="abs social social-foot" aria-label="Social links"><span></span><span></span><span></span><span></span></div>
  </footer>
</body>
</html>
```